Harbrook Techlink Solutions

We need a Logo and Website for our company based in London. We are a IT recruitment company . We provide quality resources to top IT company across UK.

Industry/Entity Type

It Company

Number of Pages Required

4 page

```html
<!DOCTYPE html>
<html lang="en">
<head>
<meta charset="utf-8">
<title>Harbrook Techlink Solutions</title>
<link rel="stylesheet" href="https://fonts.googleapis.com/css2?family=Jost:wght@500;600&family=Carlito:wght@400;700&family=Raleway:wght@500&display=swap">
<style>
  :root {
    --orange: #f5821f;
    --blue: #1a78c2;
    --footer: #1b5988;
    --bg-dark: #2f3236;
    --bg-mid: #45484c;
    --white: #ffffff;
    --rule: rgba(255,255,255,0.55);
  }
  * { margin: 0; padding: 0; box-sizing: border-box; }
  html, body { width: 1200px; height: 841px; overflow: hidden; }
  body { font-family: "Carlito", "Calibri", sans-serif; color: var(--white); background: var(--bg-dark); }
  .page { position: relative; width: 1200px; height: 841px; overflow: hidden; }
  .hero-photo {
    position: absolute; inset: 0 0 93px 0;
    background:
      radial-gradient(ellipse at 70% 70%, rgba(120,100,85,0.35), transparent 55%),
      linear-gradient(120deg, #26282b 0%, var(--bg-mid) 45%, #3b3d41 70%, #2c2d30 100%);
  }
  .brand { position: absolute; left: 57px; top: 50px; }
  .brand-name {
    display: block; width: 280px;
    font-family: "Carlito", sans-serif; font-weight: 700; font-size: 26px;
    letter-spacing: 2px; line-height: 32px; color: var(--orange);
  }
  .call { position: absolute; right: 48px; top: 46px; display: flex; align-items: center; gap: 10px; text-align: right; }
  .call-label { font-size: 13px; line-height: 14px; }
  .call-number { font-size: 16px; font-weight: 700; }
  .call-icon { width: 39px; height: 39px; border: 1.5px solid var(--white); border-radius: 50%; display: flex; align-items: center; justify-content: center; }
  .main-nav { position: absolute; left: 47px; top: 243px; width: 283px; }
  .main-nav a {
    display: block; height: 75.5px; padding: 30px 0 0 38px;
    font-family: "Raleway", sans-serif; font-weight: 500; font-size: 16px; color: var(--white);
    text-decoration: none; border-bottom: 1px solid var(--rule);
  }
  .intro { position: absolute; left: 441px; top: 333px; width: 625px; }
  .intro-title { font-family: "Jost", sans-serif; font-weight: 500; font-size: 34px; letter-spacing: 0.5px; color: var(--orange); line-height: 42px; }
  .intro-title .accent { color: var(--blue); }
  .intro-rule { height: 2px; margin: 7px 0 10px 5px; width: 620px; background: linear-gradient(90deg, rgba(255,255,255,0.6), rgba(255,255,255,0.5) 70%, transparent); }
  .intro-text { font-size: 16.5px; line-height: 23px; padding-left: 2px; }
  .btn-more {
    display: inline-block; margin: 23px 0 0 6px; width: 133px; height: 43px; line-height: 41px;
    text-align: center; background: var(--orange); border: 1px solid var(--white);
    font-size: 13px; color: var(--white); text-decoration: none;
  }
  .site-footer { position: absolute; left: 0; right: 0; bottom: 0; height: 93px; background: var(--footer); display: flex; align-items: center; justify-content: space-between; padding: 0 48px 0 47px; }
  .copyright { font-size: 13px; }
  .social { display: flex; gap: 17px; }
  .social a {
    width: 38px; height: 38px; border-radius: 50%; border: 1.5px solid var(--white);
    display: flex; align-items: center; justify-content: center;
    font-size: 10px; font-weight: 700; color: var(--white); text-decoration: none;
  }
  .social a:first-child { background: var(--white); color: var(--footer); }
</style>
</head>
<body>
<div class="page">
  <div class="hero-photo" role="img" aria-label="Photo of hands typing on a laptop at an office desk, darkened"></div>

  <header>
    <div class="brand">
      <span class="brand-name">Harbrook Techlink Solutions</span>
    </div>
    <div class="call">
      <div>
        <div class="call-label">CALL US</div>
        <div class="call-number">+44-020-555-0142</div>
      </div>
      <div class="call-icon">
        <svg width="20" height="20" viewBox="0 0 24 24" fill="none" stroke="#fff" stroke-width="2" stroke-linecap="round" stroke-linejoin="round" aria-hidden="true">
          <path d="M22 16.9v3a2 2 0 0 1-2.2 2 19.8 19.8 0 0 1-8.6-3.1 19.5 19.5 0 0 1-6-6A19.8 19.8 0 0 1 2.1 4.2 2 2 0 0 1 4.1 2h3a2 2 0 0 1 2 1.7c.1 1 .4 1.9.7 2.8a2 2 0 0 1-.5 2.1L8 9.9a16 16 0 0 0 6 6l1.3-1.3a2 2 0 0 1 2.1-.4c.9.3 1.8.6 2.8.7a2 2 0 0 1 1.7 2z"/>
          <path d="M15 5a5 5 0 0 1 4 4M15 1a9 9 0 0 1 8 8"/>
        </svg>
      </div>
    </div>
  </header>

  <nav class="main-nav">
    <a href="#">HOME</a>
    <a href="#">ABOUT US</a>
    <a href="#">SERVICES</a>
    <a href="#">BLOGS</a>
    <a href="#">CONTACT US</a>
  </nav>

  <section class="intro">
    <h1 class="intro-title">HARBROOK TECHLINK <span class="accent">SOLUTIONS</span></h1>
    <div class="intro-rule"></div>
    <p class="intro-text">Lorem ipsum dolor sit amet, consectetur adipiscing elit, sed do eiusmod tempor incididunt ut labore et doloreLorem ipsum dolor sit amet, consectetur adipiscing elit, sed do eiusmod tempor incididunt ut labore et dolore</p>
    <a class="btn-more" href="#">READ MORE</a>
  </section>

  <footer class="site-footer">
    <p class="copyright">All Right Reserved. Copyright ©2016 Harbrook Techlink Solutions</p>
    <div class="social">
      <a href="#">Vesta</a>
      <a href="#">Pipit</a>
      <a href="#">Orbo</a>
    </div>
  </footer>
</div>
</body>
</html>
```